Design for a Note buying company that attracts landlords and seller financed notes

I need a card designed. I want a simple clean front with my logo and contact info. On the back I want some big and bold words to get a message across.

Our Company buys Notes (mortgages) and we want to convey the sense of financial security. Our number one market that we pursue is tired landlords.

If you want to understand our business you can visit our website. www.lakeviewpaperfund.com

Do not use any Clip Art in the design, it will not be accepted. I want a custom designed card not something I could throw together myself. Simple clean and drive the message home.

Target Market(s)

Landlords, seller financed note holders

Industry/Entity Type

Mortgage

Contact Information for Business Card

Simple clean and bold. I need to grab the attention of the customer. It should convey a professional touch.

Font styles to use
Sans Serif

Colors
ec2229
ffffff

Requirements
Must have
• Clean front with logo and contact information
Front colors should match logo

Back should be bold and grab attention. Back colors are open to ideas
Nice to have
• The Back May use the phrase "No more Tentants, No more Toilets" "More Time, More Cash"

I'm open to other ideas about grabbing a landlords attention

I'm open to a square card design
I like cards with round corners as well
Should not have
• any clip art! must be custom designs.

```html
<!DOCTYPE html>
<html lang="en">
<head>
<meta charset="utf-8">
<title>Lakeview Paper Fund – Business Card</title>
<link rel="stylesheet" href="https://fonts.googleapis.com/css2?family=Exo+2:wght@700;800&family=Oswald:wght@500&family=Arimo:wght@400&display=swap">
<style>
  :root {
    --stage: #0e0e0e;
    --card: #1d1d1e;
    --red: #ec2229;
    --white: #ffffff;
    --grey: #9a9a9a;
    --rule: #6a6a6a;
  }
  * { box-sizing: border-box; margin: 0; padding: 0; }
  html, body { width: 1200px; height: 900px; overflow: hidden; background: var(--stage); }
  .stage {
    width: 1200px; height: 900px;
    display: flex; flex-direction: column; align-items: center; justify-content: center;
    gap: 40px;
  }
  .card {
    position: relative;
    width: 630px; height: 360px;
    background: var(--card);
    overflow: hidden;
  }
  .card::after {
    content: ""; position: absolute; left: 0; right: 0; bottom: 0;
    height: 9px; background: var(--red);
  }
  /* Front */
  .card-front {
    display: flex; flex-direction: column; align-items: center; justify-content: center;
    gap: 34px; padding-bottom: 20px;
  }
  .brand {
    display: flex; align-items: center; gap: 14px;
    font-family: "Exo 2", sans-serif; font-weight: 800;
    font-size: 38px; letter-spacing: 2px; color: var(--white);
    text-transform: uppercase;
  }
  .brand-mark { width: 18px; height: 18px; border-radius: 50%; background: var(--red); }
  .slogan {
    font-family: "Exo 2", sans-serif; font-weight: 700;
    color: var(--red); font-size: 25px; line-height: 1.3; text-align: center;
    letter-spacing: 0.5px;
  }
  /* Back */
  .card-back { padding: 80px 60px 0 70px; }
  .contact-row { display: flex; align-items: center; gap: 28px; }
  .identity { text-align: right; }
  .person-name {
    font-family: "Oswald", sans-serif; font-weight: 500;
    font-size: 34px; color: var(--red); text-transform: uppercase; line-height: 1.05;
  }
  .person-role {
    font-family: "Arimo", sans-serif; font-size: 20px; color: var(--grey); margin-top: 2px;
  }
  .divider { width: 1px; height: 92px; background: var(--rule); }
  .contact-list { list-style: none; font-family: "Arimo", sans-serif; font-size: 20px; color: var(--grey); }
  .contact-list li { display: flex; align-items: center; gap: 10px; line-height: 1.45; }
  .contact-list svg { width: 18px; height: 18px; flex: none; }
  .address {
    position: absolute; left: 70px; bottom: 48px;
    font-family: "Arimo", sans-serif; font-size: 21px; color: var(--grey);
  }
</style>
</head>
<body>
<main class="stage">
  <section class="card card-front">
    <div class="brand"><span class="brand-mark"></span>Lakeview Paper Fund</div>
    <p class="slogan">No more Tentants, No more Toilets<br>More Time, More Cash</p>
  </section>

  <section class="card card-back">
    <div class="contact-row">
      <div class="identity">
        <h1 class="person-name">Daniel Reyes</h1>
        <p class="person-role">Managing Director</p>
      </div>
      <div class="divider"></div>
      <ul class="contact-list">
        <li>
          <svg viewBox="0 0 24 24" aria-hidden="true"><path fill="var(--red)" d="M6.6 10.8a15.1 15.1 0 0 0 6.6 6.6l2.2-2.2a1 1 0 0 1 1-.25 11.4 11.4 0 0 0 3.6.57 1 1 0 0 1 1 1V20a1 1 0 0 1-1 1A17 17 0 0 1 3 4a1 1 0 0 1 1-1h3.5a1 1 0 0 1 1 1c0 1.25.2 2.45.57 3.57a1 1 0 0 1-.25 1z"/></svg>
          044-123 456 789
        </li>
        <li>
          <svg viewBox="0 0 24 24" aria-hidden="true"><rect x="2" y="5" width="20" height="14" fill="var(--red)"/><path d="M2 5l10 8 10-8" fill="none" stroke="var(--card)" stroke-width="1.6"/></svg>
          info@lakeviewpaperfund.com
        </li>
        <li>
          <svg viewBox="0 0 24 24" aria-hidden="true"><g fill="none" stroke="var(--red)" stroke-width="2"><circle cx="12" cy="12" r="9"/><ellipse cx="12" cy="12" rx="4" ry="9"/><path d="M3 12h18M5 7h14M5 17h14"/></g></svg>
          www.lakeviewpaperfund.com
        </li>
      </ul>
    </div>
    <p class="address">421, Address line here, Country Name, 45452</p>
  </section>
</main>
</body>
</html>
```